Consumer Product Goods (Food) website

We need a simple, but clean and modern website for our new food branded company called Brightfern Foods.

Need a website that company can easily update. I added company logo and some images of our products. I added 1 package design of our products that's available now in the retail stores.

Company currently has 1 item but will be adding up to 5 items witin a few months. So need a website we can easily add new products.
Updates

Project Deadline Extended
Reason: We're guaranteeing payment and wanted to give more time for others to submit.

Target Market(s)

Customers that are seeking new adventurous novelty Asian foods.

Industry/Entity Type

Retail

Coding

Coded - Design and coding required

Number of Pages Required

3 page

Requirements
Must have
• I would like to have 3 pages: Homepage, Products Page, and Contact Us.
Nice to have
• I would like a nice visually clean and modern looking homepage. As you can see from the package design, it has a dark tone, so if we can try to make the website a dark blackgroup. I uploaded the dark background we used in our package. Maybe have the 3 different dumplings rotating images on the homepage.
• Products Page should have just 1 product right now; Kimchi & Pork dumplings. Maybe have like pic of the package design and have space for a briefly summary of product, ingredient list and nutrition fact. Should be a page where i can add more products to this page.
• Contact Us page can simply have map, email addres, and phone #.
• would be nice to have where the website is responsive to PC, tablet, and mobile phones

```html
<!DOCTYPE html>
<html lang="en">
<head>
<meta charset="utf-8">
<title>Brightfern Foods</title>
<link rel="stylesheet" href="https://fonts.googleapis.com/css2?family=Open+Sans:wght@400;600;700&family=Rubik+Dirt&display=swap">
<style>
  :root {
    --bg: #292826;
    --footer: #0a0a0a;
    --green: #8fbd2f;
    --orange: #c4522b;
    --text: #e6e3de;
    --muted: #bdb8b0;
    --white: #ffffff;
    --wood-dark: #231f1b;
    --wood: #3b332b;
    --dough: #e7e0cf;
    --dough-shade: #b9ad92;
    --pepper: #b8361e;
    --leaf: #6f9a34;
    --board: #a47a4d;
    --slate: #1f2b2c;
  }
  * { margin: 0; padding: 0; box-sizing: border-box; }
  html, body { width: 1200px; height: 3136px; overflow: hidden; }
  body {
    background: var(--bg);
    color: var(--text);
    font-family: "Open Sans", Arial, sans-serif;
    position: relative;
  }
  .section { position: absolute; left: 0; width: 1200px; overflow: hidden; }

  /* Hero */
  .hero { top: 0; height: 657px; }
  .hero-photo {
    position: absolute; inset: 0;
    background:
      radial-gradient(ellipse 150px 110px at 1010px 300px, rgba(184,54,30,.85) 0%, rgba(184,54,30,0) 100%),
      radial-gradient(ellipse 170px 130px at 420px 330px, rgba(231,224,207,.95) 0%, rgba(231,224,207,0) 100%),
      radial-gradient(ellipse 190px 140px at 700px 240px, rgba(231,224,207,.9) 0%, rgba(231,224,207,0) 100%),
      radial-gradient(ellipse 200px 130px at 650px 520px, rgba(220,212,193,.9) 0%, rgba(220,212,193,0) 100%),
      radial-gradient(ellipse 160px 120px at 880px 420px, rgba(214,206,186,.85) 0%, rgba(214,206,186,0) 100%),
      radial-gradient(ellipse 150px 90px at 260px 60px, rgba(120,100,50,.7) 0%, rgba(120,100,50,0) 100%),
      radial-gradient(ellipse 560px 340px at 640px 360px, #1c1b1a 0%, #151413 88%, rgba(21,20,19,0) 100%),
      linear-gradient(100deg, #3a3029 0%, #4a3e33 40%, #3b3129 70%, #2c241f 100%);
  }
  .hero-shade { position: absolute; inset: 0; background: rgba(0,0,0,.18); }
  .nav-bar { position: absolute; left: 75px; right: 75px; top: 0; height: 92px; border-bottom: 1px solid rgba(255,255,255,.35); }
  .nav-link { position: absolute; top: 36px; font-size: 13px; font-weight: 700; color: var(--white); text-transform: uppercase; }
  .nav-link.active { color: var(--green); }
  .nav-underline { position: absolute; left: 0; top: 64px; width: 92px; height: 3px; background: var(--green); }
  .nav-phone { position: absolute; left: 711px; top: 33px; font-size: 17px; font-weight: 700; color: var(--white); display: flex; align-items: center; gap: 6px; }
  .social-dot { position: absolute; width: 15px; height: 15px; border-radius: 50%; background: var(--green); }
  .brand { position: absolute; left: 0; width: 1200px; top: 148px; text-align: center; }
  .brand-mark { width: 134px; height: 134px; margin: 0 auto; background: var(--green); border-radius: 24px; }
  .brand-name { margin-top: 28px; font-weight: 700; font-size: 50px; line-height: 1; color: var(--white); text-transform: uppercase; letter-spacing: 1px; }
  .hero-tagline { position: absolute; left: 0; width: 1200px; top: 418px; text-align: center; font-family: "Rubik Dirt", "Open Sans", sans-serif; font-weight: 400; font-size: 38px; line-height: 46px; color: var(--white); text-transform: uppercase; letter-spacing: 1px; }
  .slider-dots { position: absolute; left: 0; width: 1200px; top: 580px; display: flex; justify-content: center; gap: 12px; }
  .slider-dots span { width: 14px; height: 14px; border-radius: 50%; background: var(--white); }
  .slider-dots span.current { background: var(--green); }

  /* Shared */
  .section-head { position: absolute; left: 0; width: 1200px; text-align: center; }
  .section-mark { width: 42px; height: 42px; margin: 0 auto; background: var(--green); border-radius: 9px; }
  .section-title { margin-top: 8px; font-family: "Rubik Dirt", "Open Sans", sans-serif; font-weight: 400; font-size: 44px; line-height: 56px; color: var(--white); text-transform: uppercase; letter-spacing: 1px; }
  .section-rule { width: 78px; height: 4px; margin: 8px auto 0; background: var(--green); }
  .btn {
    position: absolute; height: 52px; width: 209px;
    background: var(--orange); color: var(--white);
    font-size: 16px; font-weight: 700; text-transform: uppercase;
    display: flex; align-items: center; justify-content: center;
  }

  /* About */
  .about { top: 657px; height: 503px; background: linear-gradient(180deg, #2b2a28 0%, #262523 100%); }
  .about-text { position: absolute; left: 180px; width: 840px; top: 222px; text-align: center; font-size: 16.5px; line-height: 33px; color: var(--text); }

  /* Product */
  .product { top: 1160px; height: 680px; background: linear-gradient(180deg, #2e2a26 0%, #3a332c 45%, #2a2622 75%, #1f1c1a 100%); }
  .feature-title { position: absolute; top: 206px; width: 310px; font-size: 23px; line-height: 31px; font-weight: 700; color: var(--green); }
  .feature-text { position: absolute; top: 276px; width: 310px; font-size: 16px; line-height: 26px; color: var(--text); }
  .feature-left { left: 75px; }
  .feature-right { left: 815px; text-align: right; }
  .product-photo {
    position: absolute; left: 387px; top: 209px; width: 449px; height: 282px; border-radius: 50%;
    background:
      radial-gradient(ellipse 70px 55px at 120px 190px, rgba(150,70,130,.9) 0%, rgba(150,70,130,0) 100%),
      radial-gradient(ellipse 110px 60px at 230px 40px, rgba(111,154,52,.95) 0%, rgba(111,154,52,0) 100%),
      radial-gradient(ellipse 90px 60px at 150px 110px, rgba(226,214,186,.95) 0%, rgba(226,214,186,0) 100%),
      radial-gradient(ellipse 90px 60px at 320px 110px, rgba(226,214,186,.95) 0%, rgba(226,214,186,0) 100%),
      radial-gradient(ellipse 90px 60px at 240px 190px, rgba(220,205,170,.95) 0%, rgba(220,205,170,0) 100%),
      radial-gradient(ellipse at 50% 55%, #1a1918 0%, #121110 70%, #0d0c0c 100%);
    box-shadow: 0 18px 30px rgba(0,0,0,.45);
  }

  /* Newsletter */
  .newsletter { top: 1840px; height: 412px; }
  .newsletter-photo {
    position: absolute; inset: 0;
    background:
      radial-gradient(ellipse 110px 60px at 170px 360px, rgba(184,54,30,.8) 0%, rgba(184,54,30,0) 100%),
      radial-gradient(ellipse 200px 120px at 1000px 70px, rgba(60,100,40,.85) 0%, rgba(60,100,40,0) 100%),
      radial-gradient(ellipse 130px 60px at 560px 20px, rgba(184,54,30,.6) 0%, rgba(184,54,30,0) 100%),
      radial-gradient(ellipse 300px 210px at 600px 225px, #b28858 0%, #a47a4d 70%, rgba(164,122,77,0) 100%),
      linear-gradient(90deg, #1d2627 0%, #243031 25%, #2a2a26 50%, #243031 75%, #1c2424 100%);
  }
  .email-field {
    position: absolute; left: 324px; top: 256px; width: 491px; height: 54px;
    background: var(--white); display: flex; align-items: center; padding-left: 18px; gap: 14px;
    font-size: 14px; color: #6f6f6f;
  }
  .email-go {
    position: absolute; left: 815px; top: 256px; width: 63px; height: 54px;
    background: var(--orange); color: var(--white); font-size: 22px; font-weight: 700;
    display: flex; align-items: center; justify-content: center;
  }

  /* Blog */
  .blog { top: 2252px; height: 647px; background: linear-gradient(180deg, #282725 0%, #2b2a28 100%); }
  .blog-photo {
    position: absolute; left: 75px; top: 235px; width: 512px; height: 347px;
    background:
      radial-gradient(ellipse 100px 60px at 120px 320px, rgba(150,70,130,.9) 0%, rgba(150,70,130,0) 100%),
      radial-gradient(ellipse 130px 70px at 180px 240px, rgba(226,214,186,.95) 0%, rgba(226,214,186,0) 100%),
      radial-gradient(ellipse 140px 80px at 380px 250px, rgba(226,214,186,.95) 0%, rgba(226,214,186,0) 100%),
      radial-gradient(ellipse 90px 60px at 60px 190px, rgba(184,80,40,.8) 0%, rgba(184,80,40,0) 100%),
      linear-gradient(90deg, #c4522b 0%, #c4522b 34%, #8fbd2f 34%, #8fbd2f 100%) top / 100% 150px no-repeat,
      linear-gradient(180deg, #2c2622 0%, #1c1917 100%);
  }
  .blog-title { position: absolute; left: 623px; top: 230px; width: 480px; font-size: 24px; line-height: 32px; font-weight: 700; color: var(--green); }
  .blog-text { position: absolute; left: 623px; top: 296px; width: 500px; font-size: 16.5px; line-height: 32px; color: var(--text); }

  /* Footer */
  .footer { top: 2899px; height: 237px; background: var(--footer); }
  .footer-nav { position: absolute; top: 50px; font-size: 15px; font-weight: 600; color: var(--white); text-transform: uppercase; transform: translateX(-50%); white-space: nowrap; }
  .footer-copy { position: absolute; left: 0; width: 1200px; top: 94px; text-align: center; font-size: 12.5px; color: var(--muted); }
  .footer .social-dot { top: 145px; }
</style>
</head>
<body>

<header class="section hero">
  <div class="hero-photo" role="img" aria-label="Steamed dumplings on a dark plate with sliced red pepper and chives on a wooden table"></div>
  <div class="hero-shade"></div>
  <nav class="nav-bar">
    <span class="nav-link active" style="left:25px">Home</span>
    <span class="nav-underline"></span>
    <span class="nav-link" style="left:117px">About Us</span>
    <span class="nav-link" style="left:234px">Product</span>
    <span class="nav-link" style="left:345px">Blog</span>
    <span class="nav-link" style="left:431px">Contact Us</span>
    <span class="nav-phone">
      <svg width="16" height="16" viewBox="0 0 24 24"><path fill="#fff" d="M6.6 10.8a15.1 15.1 0 0 0 6.6 6.6l2.2-2.2c.3-.3.7-.4 1-.2 1.1.4 2.3.6 3.6.6.6 0 1 .4 1 1V20c0 .6-.4 1-1 1A17 17 0 0 1 3 4c0-.6.4-1 1-1h3.5c.6 0 1 .4 1 1 0 1.3.2 2.5.6 3.6.1.3 0 .7-.2 1z"/></svg>
      1-800-555-0147
    </span>
    <span class="social-dot" style="left:895px; top:36px"></span>
    <span class="social-dot" style="left:931px; top:36px"></span>
    <span class="social-dot" style="left:968px; top:36px"></span>
    <span class="social-dot" style="left:1006px; top:36px"></span>
    <span class="social-dot" style="left:1043px; top:36px"></span>
  </nav>
  <div class="brand">
    <div class="brand-mark"></div>
    <div class="brand-name">Brightfern Foods</div>
  </div>
  <h1 class="hero-tagline">We are a novelty Asian foods restaurant</h1>
  <div class="slider-dots"><span class="current"></span><span></span><span></span><span></span></div>
</header>

<section class="section about">
  <div class="section-head" style="top:56px">
    <div class="section-mark"></div>
    <h2 class="section-title">About Us</h2>
    <div class="section-rule"></div>
  </div>
  <p class="about-text">Inspired by the name of a famous trade route that connected East Asia and Western countries, Brightfern Foods was created to bring traditional and exceptional Asian cuisine to the markets around the globe. Brightfern's mission is to provide most clean, delicious, and convenient foods to our customers andis committed to promoting healthier lifestyle and sustainability.</p>
  <span class="btn" style="left:496px; top:392px">Read More</span>
</section>

<section class="section product">
  <div class="section-head" style="top:30px">
    <div class="section-mark"></div>
    <h2 class="section-title">Product</h2>
    <div class="section-rule"></div>
  </div>
  <h3 class="feature-title feature-left">History and Exceptional flavor of Kimchi</h3>
  <p class="feature-text feature-left">Kimchi, a reddish fermented cabbage mixed with variety of spices like garlic and ginger, was originally developed more than 3K years ago as a way to preserve vegetables over long winter. Kimchi is now Korea's national dish and is rapidly growing popularity all over the world.</p>
  <div class="product-photo" role="img" aria-label="Pan-fried kimchi and pork dumplings on a black plate with lettuce and red onion"></div>
  <h3 class="feature-title feature-right">How big is this dumpling?</h3>
  <p class="feature-text feature-right">Weighing in at around 70 grams per piece, Kimchi &amp; Pork LARGE size dumplings will be the BIGGEST dumpling you have ever tried. Packed with Kimchi, Pork, Noodles, and other Vegetables, you'll surely become a fan once take the first bite.</p>
  <span class="btn" style="left:496px; top:550px">Read More</span>
</section>

<section class="section newsletter">
  <div class="newsletter-photo" role="img" aria-label="Wooden cutting board on a dark table with chili peppers, garlic, herbs and spices"></div>
  <div class="section-head" style="top:90px">
    <div class="section-mark"></div>
    <h2 class="section-title">Product</h2>
    <div class="section-rule"></div>
  </div>
  <label class="email-field">
    <svg width="26" height="22" viewBox="0 0 26 22"><path fill="#b5b5b5" d="M0 10 25 0 20 21 12 15 9 21 8 13z"/></svg>
    Enter Email Address
  </label>
  <span class="email-go">GO</span>
</section>

<section class="section blog">
  <div class="section-head" style="top:60px">
    <div class="section-mark"></div>
    <h2 class="section-title">Recent Blog</h2>
    <div class="section-rule"></div>
  </div>
  <div class="blog-photo" role="img" aria-label="Kimchi and pork dumplings package artwork with dumplings and a fork"></div>
  <h3 class="blog-title">Duis aliquam nibh a dui iaculis viverra id a velit</h3>
  <p class="blog-text">Nunc consequat congue nulla eu imperdiet. Donec in est erat, id malesuada turpis. Nunc a dui id turpis convallis semper. Nunc dignissim lectus vitae eros placerat magna vel eros adipiscing adipiscing eu sit amet turpis. Vestibulum vel metus sit amet turpis bibendum tincidunt vel sit amet quam..</p>
  <span class="btn" style="left:623px; top:486px">Read More</span>
</section>

<footer class="section footer">
  <span class="footer-nav" style="left:349px">Home</span>
  <span class="footer-nav" style="left:464px">About Us</span>
  <span class="footer-nav" style="left:592px">Product</span>
  <span class="footer-nav" style="left:705px">Blog</span>
  <span class="footer-nav" style="left:828px">Contact Us</span>
  <p class="footer-copy">Copyright © 2016. Company Name. All Right Reserved</p>
  <span class="social-dot" style="left:518px"></span>
  <span class="social-dot" style="left:553px"></span>
  <span class="social-dot" style="left:590px"></span>
  <span class="social-dot" style="left:626px"></span>
  <span class="social-dot" style="left:663px"></span>
</footer>

</body>
</html>
```